Contemporary restaurant add that stands out

I would like an ad that I can use for flyers and in guide books for a tourist restaurant. It must reflect high quality, be contemporary and stand out amongst other adverts.

The ad must try and say good quality food in pleasant surroundings.

The ad must be left open because different guide books require different size ads, so it must be able to resize.

I have included our current ad. I want it changed because some feedback I received say it looks more like a nightclub than a restaurant.

I also have more pics if necessary. Also I have pics of the restaurant in different colours

Target Market(s)

Tourists of various nationalities

Industry/Entity Type

Restaurant

Requirements
Must have
• The name of the restaurant is
• Paper Kite
• And it is in Edwardian script font with bold and italic selected.
• The ad must contain our phone number, address and free wifi. The details are on our current ad which is included

```html
<!DOCTYPE html>
<html lang="en">
<head>
<meta charset="utf-8">
<title>Paper Kite Restaurant Advert</title>
<link rel="stylesheet" href="https://fonts.googleapis.com/css2?family=Great+Vibes&family=Playfair+Display:ital,wght@1,700&family=Lato:wght@700;900&display=swap">
<style>
  :root {
    --wine: #7a1d3a;
    --wine-deep: #4c0f24;
    --wine-light: #9a3050;
    --stripe: rgba(255, 240, 225, 0.05);
    --ink: #141011;
    --cream: #fbf3e6;
    --gold: #d9b46a;
    --rose: #e2708f;
    --subtitle: #f0d9b0;
  }
  html, body { margin: 0; padding: 0; overflow: hidden; background: #f2f2f2; }
  .advert {
    position: relative;
    width: 861px;
    height: 1200px;
    overflow: hidden;
    background:
      repeating-linear-gradient(180deg, var(--stripe) 0 24px, transparent 24px 60px),
      linear-gradient(165deg, var(--wine-light), var(--wine) 45%, var(--wine-deep));
    font-family: "Lato", Arial, sans-serif;
  }
  .website {
    position: absolute; top: 106px; left: 0; width: 100%;
    text-align: center; color: var(--cream);
    font-family: "Playfair Display", Georgia, serif; font-style: italic; font-weight: 700;
    font-size: 27px; line-height: 40px;
  }
  .wifi-badge {
    position: absolute; top: 52px; left: 680px; width: 100px;
    color: var(--cream); text-align: center;
  }
  .wifi-badge .free { font-weight: 900; font-size: 22px; line-height: 26px; letter-spacing: 1px; }
  .wifi-badge .wifi-box {
    margin: 4px auto 0; width: 100px; height: 46px; border-radius: 12px;
    background: var(--ink); display: flex; align-items: center; justify-content: center; gap: 5px;
    font-weight: 900; font-size: 25px;
  }
  .title-swoosh { position: absolute; top: 250px; left: 0; }
  .subtitle {
    position: absolute; top: 222px; left: 0; width: 100%; text-align: center;
    font-family: "Playfair Display", Georgia, serif; font-style: italic; font-weight: 700;
    font-size: 48px; line-height: 60px; color: var(--subtitle);
  }
  .brand-name {
    position: absolute; top: 276px; left: 0; width: 100%; text-align: center;
    font-family: "Great Vibes", cursive; font-size: 160px; line-height: 170px; color: var(--cream);
    white-space: nowrap;
  }
  .photo { position: absolute; }
  .photo-interior { left: 0; top: 517px; width: 356px; height: 224px;
    background: linear-gradient(135deg, #2f5a3e, #7b6a4a 50%, #c9a46a); }
  .photo-grill { left: 366px; top: 517px; width: 495px; height: 224px;
    background: radial-gradient(circle at 45% 45%, #8a3b1c, #3a1208 60%, #e0631b); }
  .photo-fish { left: 0; top: 749px; width: 356px; height: 176px;
    background: linear-gradient(160deg, #f2ede2, #d8c9a8 60%, #6e8a3c); }
  .photo-terrace { left: 366px; top: 749px; width: 495px; height: 176px;
    background: linear-gradient(180deg, #1c0e2a, #5a2a3a 55%, #d9a066); }
  .contact-band {
    position: absolute; top: 970px; left: 0; width: 100%; height: 172px; background: var(--ink);
    border-top: 2px solid var(--gold); border-bottom: 2px solid var(--gold);
  }
  .address {
    position: absolute; top: 988px; left: 0; width: 100%; text-align: center;
    font-family: "Playfair Display", Georgia, serif; font-weight: 700; font-style: italic;
    font-size: 25px; line-height: 32px; color: var(--gold);
  }
  .reservations {
    position: absolute; top: 1064px; left: 0; width: 100%; text-align: center;
    color: var(--cream); font-weight: 900; font-size: 36px; line-height: 48px;
  }
</style>
</head>
<body>
<main class="advert">
  <div class="website">www.paperkite-dining.com</div>

  <div class="wifi-badge">
    <div class="free">FREE</div>
    <div class="wifi-box">
      <svg width="26" height="22" viewBox="0 0 30 26" aria-hidden="true">
        <path d="M2 9 A19 19 0 0 1 28 9" fill="none" stroke="#fbf3e6" stroke-width="3.5" stroke-linecap="round"/>
        <path d="M7 14 A12 12 0 0 1 23 14" fill="none" stroke="#fbf3e6" stroke-width="3.5" stroke-linecap="round"/>
        <path d="M11.5 19 A5.5 5.5 0 0 1 18.5 19" fill="none" stroke="#fbf3e6" stroke-width="3.5" stroke-linecap="round"/>
        <circle cx="15" cy="23" r="2.3" fill="#fbf3e6"/>
      </svg>
      <span>WiFi</span>
    </div>
  </div>

  <svg class="title-swoosh" width="861" height="200" viewBox="0 0 861 200" aria-hidden="true">
    <path d="M0 130 C220 60 580 50 861 100 L861 140 C580 100 230 115 0 180 Z" fill="rgba(217,180,106,0.14)"/>
    <path d="M0 160 C260 105 580 105 861 125 L861 134 C580 120 260 125 0 172 Z" fill="rgba(217,180,106,0.35)"/>
  </svg>
  <div class="subtitle">Restaurant</div>
  <div class="brand-name">Paper Kite</div>

  <div class="photo photo-interior" role="img" aria-label="Photo of the restaurant dining room with plants and lounge seating"></div>
  <div class="photo photo-grill" role="img" aria-label="Photo of steaks cooking over a flaming grill"></div>
  <div class="photo photo-fish" role="img" aria-label="Photo of grilled fish fillets with lemon and dipping sauces"></div>
  <div class="photo photo-terrace" role="img" aria-label="Photo of the illuminated restaurant terrace at night"></div>

  <div class="contact-band"></div>
  <div class="address">Paseo del Faro, C.C. Marisol,<br>Playa de la Bahía Costa Serena</div>
  <div class="reservations">For Reservations: 900 41 63 58</div>
</main>
</body>
</html>
```